Aquatic View

We need a web design for a new window cleaning company name Bright Pane Services. We are located in Grand Cayman, Cayman Islands. We are a small company, a team of husband and wife. Our services include residencial interior and exterior window cleaning and commercial. Extra services such as ceiling fans cleaning, mirrors, high dusting. Home cleaning services. Power washing. Explaining the service. We want a modern, beachy style with aquatic colors. We want to use our domain name "brightpaneservices.ky". We want to portray a clean, modern and professional design.

Target Market(s)

Big Home owners

Industry/Entity Type

Cleaning Service

Contact Information for Business Card

Company Name: Bright Pane Services
Name: Gerald Thornbury owner/manager
Phone: 345-9418372
Email: gerald@brightpaneservices.ky
Website: brightpaneservices.ky
Address: P.O.Box 2846 GT, George Town, Grand Cayman KY1-1304 Cayman Islands

Number of Pages Required

2 page

Font styles to use
Sans Serif

Colors
0592cd
0455a3
33a6d7
85cae6
cadf82
abd036
fbf289

Requirements
Nice to have
• Pictures of an ocean view and palm trees from clear windows.
• https://quotrelvane.com/estimately/
• Use the above for "free estimate".

```html
<!DOCTYPE html>
<html lang="en">
<head>
<meta charset="utf-8">
<title>Bright Pane Services</title>
<link href="https://fonts.googleapis.com/css2?family=Lato:wght@400;700&family=Fira+Sans:wght@500;600&display=swap" rel="stylesheet">
<style>
:root{
  --brand-blue:#0a8fd0;
  --deep-blue:#0455a3;
  --accent-red:#c4121c;
  --navy:#16355c;
  --navy-circle:rgba(22,48,86,.9);
  --text:#5a5a5a;
  --dark:#222;
  --footer:#1f1f1f;
  --line:#d9d9d9;
}
*{box-sizing:border-box;margin:0;padding:0}
html,body{width:1200px;height:1071px;overflow:hidden}
body{position:relative;font-family:"Lato",sans-serif;color:var(--text);background:#fff}
.abs{position:absolute}

.top-bar{left:0;top:0;width:1200px;height:34px;background:linear-gradient(90deg,#3f5f88,#5c7faa 50%,#3d5d86)}
.top-phone{right:116px;top:5px;color:#fff;font-size:20px;font-weight:700;display:flex;align-items:center;gap:6px}
.top-phone svg{width:26px;height:26px}

.header{left:0;top:34px;width:1200px;height:69px;background:#fff}
.brand{left:120px;top:52px;display:flex;align-items:center;gap:8px;font-size:19px;font-weight:700;color:var(--navy);font-family:"Lato",sans-serif}
.brand-dot{width:22px;height:22px;border-radius:50%;background:var(--brand-blue)}
.nav{left:728px;top:62px;display:flex;align-items:center;font-size:13px;font-weight:700;letter-spacing:.3px;color:var(--dark)}
.nav a{color:inherit;text-decoration:none;padding:4px 12px;border-right:1px solid #ccc;line-height:14px}
.nav a:last-child{border-right:0}
.nav a.active{color:var(--brand-blue);border:1px solid var(--brand-blue);padding:4px 12px}
.nav .sp{margin-left:4px}

.hero{left:0;top:103px;width:1200px;height:501px;background:radial-gradient(ellipse at 40% 50%,#9fb7d2 0%,#6f93bd 45%,#4c74a6 100%)}
.hero-title{right:510px;top:196px;text-align:right;font-family:"Fira Sans",sans-serif;font-weight:600;font-size:30px;line-height:43px;color:#fff}
.circle{border-radius:50%;background:var(--navy-circle);width:172px;height:172px;display:flex;flex-direction:column;align-items:center;justify-content:center;color:#fff;font-family:"Fira Sans",sans-serif;font-weight:600;font-size:19px;text-align:center;line-height:21px}
.circle svg{width:58px;height:52px;margin-bottom:12px}
.c-res{left:721px;top:171px}
.c-com{left:867px;top:214px}
.c-oth{left:758px;top:313px}
.arrow{width:34px;height:34px;border-radius:50%;background:#fff;box-shadow:0 1px 4px rgba(0,0,0,.4);display:flex;align-items:center;justify-content:center}
.arrow svg{width:14px;height:14px}
.arrow-l{left:34px;top:334px}
.arrow-r{left:1131px;top:334px}

.below{left:0;top:604px;width:1200px;height:318px;background:linear-gradient(#dcdcdc,#f4f4f4 60%,#fff)}
.panel{left:99px;top:573px;width:1002px;height:349px;background:#fff}

.col h2{font-family:"Lato",sans-serif;font-weight:700;font-size:17px;letter-spacing:1px;color:var(--brand-blue);white-space:nowrap}
.col h2 span{color:var(--accent-red)}
.rule{height:1px;background:var(--line);margin-top:10px;position:relative}
.rule::before{content:"";position:absolute;left:0;top:-1px;width:86px;height:2px;background:var(--brand-blue)}
.col p{font-size:13px;line-height:19px}
.btn{display:inline-block;background:linear-gradient(#0d77c4,#0455a3);color:#fff;font-weight:700;font-size:13px;padding:9px 9px;line-height:13px}

.col-about{left:116px;top:598px;width:266px}
.about-photo{margin-top:13px;width:266px;height:121px;border:1px solid #aaa;background:linear-gradient(90deg,#d9e1e8,#9fb3c4 40%,#6c8aa6 60%,#d4dbe2)}
.col-about p{margin-top:11px;color:#666}
.col-about .btn{margin-top:11px}

.v-sep{width:1px;background:#eee;top:612px;height:258px}

.col-services{left:433px;top:598px;width:334px}
.col-services .intro{margin-top:13px;padding-left:2px}
.svc{margin-top:9px;position:relative;padding-left:27px}
.svc svg{position:absolute;left:0;top:0;width:20px;height:18px}
.svc h3{font-size:15px;font-weight:700;color:var(--brand-blue);line-height:18px}
.svc p{margin-top:0}

.col-inquiry{left:817px;top:598px;width:265px}
.field{margin-top:10px;border:1px solid #ccc;height:30px;font-size:12px;padding:7px 6px;color:#555}
.field:first-of-type{margin-top:17px}
.field-first{margin-top:16px}
.field-msg{height:73px;margin-top:7px}
.col-inquiry .btn{margin-top:9px;padding:10px 20px}

.footer{left:0;top:922px;width:1200px;height:107px;background:var(--footer);color:#fff}
.f-nav{left:117px;top:943px;font-size:13px;font-weight:700;color:#fff;display:flex;gap:0}
.f-nav span{padding-right:9px}
.f-nav .bar{padding:0 12px 0 0}
.f-line{left:116px;font-size:13px;color:#eee;display:flex;align-items:center;gap:7px}
.f-line svg{width:14px;height:14px}
.subscribe{left:841px;top:941px;width:243px;height:30px;display:flex;border-radius:2px;overflow:hidden}
.subscribe .in{flex:1;background:#fff;font-size:11px;font-style:italic;color:#999;display:flex;align-items:center;gap:6px;padding-left:8px}
.subscribe .go{width:84px;background:linear-gradient(#0d77c4,#0455a3);color:#fff;font-weight:700;font-size:13px;display:flex;align-items:center;justify-content:center}
.social{left:969px;top:989px;display:flex;gap:6px}
.social i{display:block;width:24px;height:24px;border:1.5px solid #ddd;border-radius:50%}
.copy{left:0;top:1029px;width:1200px;height:42px;background:linear-gradient(#0d7fc8,#0455a3);color:#fff;font-size:13px;text-align:center;line-height:42px}
</style>
</head>
<body>

<div class="abs top-bar" role="img" aria-label="Soapy glass texture strip"></div>
<div class="abs top-phone">
  <svg viewBox="0 0 26 26" fill="none" stroke="#fff" stroke-width="1.6"><circle cx="13" cy="13" r="11.5"/><path d="M9 7.5l2 3-1.3 1.3c.8 1.8 2 3 3.7 3.8L14.7 14l3 2-1.2 2.2c-4.6-.6-8.2-4.3-8.8-8.8z" fill="#fff"/></svg>
  345-941-8372
</div>

<div class="abs header"></div>
<div class="abs brand"><i class="brand-dot"></i>Bright Pane Services</div>
<nav class="abs nav">
  <a class="active" href="#">HOME</a>
  <a class="sp" href="#">ABOUT US</a>
  <a href="#">SERIVCES</a>
  <a href="#" style="padding-left:20px">CONTACT US</a>
</nav>

<section class="abs hero" role="img" aria-label="Squeegee wiping soapy water across a window pane"></section>
<h1 class="abs hero-title">Interior And Exterior<br>Window Cleaning And<br>Other Cleaning Services</h1>

<div class="abs circle c-res">
  <svg viewBox="0 0 58 52" fill="#fff"><path d="M6 14h46l4 8H2z"/><rect x="12" y="4" width="6" height="10"/><rect x="6" y="22" width="46" height="28"/><g fill="#16355c"><rect x="12" y="28" width="6" height="6"/><rect x="22" y="28" width="6" height="6"/><rect x="32" y="28" width="6" height="6"/><rect x="42" y="28" width="6" height="6"/><rect x="12" y="38" width="6" height="6"/><rect x="26" y="38" width="6" height="12"/><rect x="42" y="38" width="6" height="6"/></g></svg>
  RESIDENTIAL
</div>
<div class="abs circle c-com">
  <svg viewBox="0 0 58 52" fill="#fff"><rect x="2" y="0" width="20" height="52"/><rect x="26" y="16" width="30" height="36"/><g stroke="#16355c" stroke-width="2"><path d="M5 6h14M5 12h14M5 18h14M5 24h14M5 30h14M5 36h14M5 42h14M29 22h24M29 28h24M29 34h24M29 40h24M29 46h24M36 16v36M46 16v36"/></g></svg>
  COMMERCIAL
</div>
<div class="abs circle c-oth">
  <svg viewBox="0 0 58 52" fill="none" stroke="#fff" stroke-width="2.5"><path d="M14 0v26"/><path d="M4 50l4-24h12l4 24z" fill="#fff"/><path d="M28 22h24l-3 28H31z"/><circle cx="34" cy="14" r="3"/><circle cx="42" cy="10" r="4"/><circle cx="48" cy="17" r="2.5"/></svg>
  OTHER<br>SERVICES
</div>
<div class="abs arrow arrow-l"><svg viewBox="0 0 14 14"><path d="M9 2L4 7l5 5" fill="none" stroke="#333" stroke-width="2.5"/></svg></div>
<div class="abs arrow arrow-r"><svg viewBox="0 0 14 14"><path d="M5 2l5 5-5 5" fill="none" stroke="#333" stroke-width="2.5"/></svg></div>

<div class="abs below"></div>
<div class="abs panel"></div>

<section class="abs col col-about">
  <h2><span>ABOUT</span> BRIGHT PANE SERVICES</h2>
  <div class="rule"></div>
  <div class="about-photo" role="img" aria-label="Worker in blue cleaning a large window with a squeegee"></div>
  <p>Lorem ipsum dolor sit amet, consectetuer adip iscing elit, sed diam nonummy nibh euismod magna aliquam erat volutpat.</p>
  <a class="btn" href="#">READ MORE</a>
</section>

<div class="abs v-sep" style="left:407px"></div>
<div class="abs v-sep" style="left:793px"></div>

<section class="abs col col-services">
  <h2><span>OUR</span> SERVICES</h2>
  <div class="rule"></div>
  <p class="intro">Lorem ipsum dolor sit amet, consectetuer adip iscing elit sed diam nonummy nibh euismod magna.</p>
  <div class="svc">
    <svg viewBox="0 0 20 18" fill="#777"><path d="M10 1L0 8h3v10h14V8h3z"/></svg>
    <h3>Residential</h3>
    <p>Lorem ipsum dolor sit amet, consectetuer adip iscing elit sed diam nonummy nibh euismod magna.</p>
  </div>
  <div class="svc">
    <svg viewBox="0 0 20 18" fill="#777"><rect x="1" y="2" width="7" height="16"/><rect x="10" y="6" width="9" height="12"/></svg>
    <h3>Commercial</h3>
    <p>Lorem ipsum dolor sit amet, consectetuer adip iscing elit sed diam nonummy nibh euismod magna.</p>
  </div>
  <div class="svc" style="margin-top:10px">
    <svg viewBox="0 0 20 18" fill="#777"><circle cx="7" cy="7" r="5"/><circle cx="15" cy="13" r="4"/><circle cx="7" cy="7" r="2" fill="#fff"/><circle cx="15" cy="13" r="1.5" fill="#fff"/></svg>
    <h3>Extra Services</h3>
    <p>Lorem ipsum dolor sit amet, consectetuer adip iscing elit sed diam nonummy nibh euismod magna.</p>
  </div>
</section>

<section class="abs col col-inquiry">
  <h2><span>QUICK</span> INQUIRY</h2>
  <div class="rule"></div>
  <div class="field field-first">Email</div>
  <div class="field" style="margin-top:7px">Phone</div>
  <div class="field" style="margin-top:8px">Email</div>
  <div class="field field-msg">Message</div>
  <a class="btn" href="#">SUBMIT</a>
</section>

<footer class="abs footer"></footer>
<div class="abs f-nav"><span>Home</span><span class="bar">I</span><span>About Us</span><span class="bar">I</span><span style="padding-right:18px">Serivces</span><span class="bar">I</span><span>Contact Us</span></div>
<div class="abs f-line" style="top:970px">
  <svg viewBox="0 0 14 14" fill="#bbb"><path d="M7 0a5 5 0 0 0-5 5c0 4 5 9 5 9s5-5 5-9a5 5 0 0 0-5-5zm0 7a2 2 0 1 1 0-4 2 2 0 0 1 0 4z"/></svg>
  Lorem ipsum dolor sit amet consectetuer adimpisciged
</div>
<div class="abs f-line" style="top:994px">
  <svg viewBox="0 0 14 14" fill="none" stroke="#bbb" stroke-width="1.2"><circle cx="7" cy="7" r="6.3"/><path d="M5 4l1 1.5-.7.8c.5 1 1.1 1.6 2 2l.8-.7L9.6 8.6 9 9.8C6.7 9.4 4.6 7.3 4.2 5z" fill="#bbb"/></svg>
  <span style="letter-spacing:.6px">345-941-8372</span>
  <svg viewBox="0 0 14 14" style="margin-left:4px;width:11px"><rect x="1" y="3" width="12" height="8" fill="#bbb"/><path d="M1 3l6 5 6-5" fill="none" stroke="#1f1f1f"/></svg>
  info@brightpaneservices.ky
</div>
<div class="abs subscribe">
  <div class="in"><svg viewBox="0 0 16 12" width="16" height="12"><rect x=".5" y=".5" width="15" height="11" fill="none" stroke="#ccc"/><path d="M.5 .5l7.5 6 7.5-6" fill="none" stroke="#ccc"/></svg>your e-mail address</div>
  <div class="go">SUBSCRIBE</div>
</div>
<div class="abs social"><i></i><i></i><i></i><i></i></div>

<div class="abs copy">Copyright © 2015&nbsp; BrightPaneServices. All Right Reserved</div>

</body>
</html>
```